Animal Eye Clinic needs a Business card

We are a new veterinary ophthalmology practice (Silverbrook Pet Vision Care) and we need a business card designed. We only see animal eyes - we are not a regular veterinary clinic. We already have a logo. We are looking for a professional, good looking business card to hand out to our clients. We are looking for something simple but professional and contemporary. Our logo is likely the only picture/graphic that needs to be on the card.

Contact Information for Business Card

Marisol Quent, BSc, DVM, MSc, DipACVO
Veterinary Ophthalmologist

Phone: 250.419.3067
Email: silverbrookpetvisioncare@mailvero.com
Website: silverbrookpetvisioncare.com
Address: 1875 Tessock Rd
Kelowna, BC, V4T 8M3

Colors

Designer to choose colors to be used in the design.

Requirements
Must have
• Our logo (attached)

```html
<!DOCTYPE html>
<html lang="en">
<head>
<meta charset="utf-8">
<title>Silverbrook Pet Vision Care – Business Card</title>
<link rel="stylesheet" href="https://fonts.googleapis.com/css2?family=Lato:wght@400;700;900&display=swap">
<style>
  :root {
    --teal: #0f9aa8;
    --teal-deep: #0b7f8b;
    --charcoal: #2f3236;
    --paper: #f7f8f8;
    --ink-grey: #5b5f63;
    --stage: #2a2b2d;
    --white: #ffffff;
    --light-ink: #e4e6e7;
  }
  * { margin: 0; padding: 0; box-sizing: border-box; }
  html, body {
    width: 1200px; height: 997px; overflow: hidden;
    background: var(--stage);
    font-family: "Lato", Arial, sans-serif;
  }
  .canvas { position: relative; width: 1200px; height: 997px; }

  .card {
    position: absolute;
    width: 560px; height: 320px;
    overflow: hidden;
    box-shadow: 0 14px 30px rgba(0,0,0,0.45);
  }

  /* Back of card */
  .card-back { left: 80px; top: 150px; background: var(--teal); }
  .card-back .brand {
    position: absolute; inset: 0;
    display: flex; flex-direction: column; align-items: center; justify-content: center; gap: 18px;
  }
  .card-back .brand-dot {
    width: 64px; height: 64px; border-radius: 50%; background: var(--white);
  }
  .card-back .brand-name {
    color: var(--white); font-weight: 900; font-size: 28px; letter-spacing: 0.5px;
  }

  /* Front of card */
  .card-front { left: 560px; top: 520px; background: var(--paper); }
  .card-front .shapes { position: absolute; inset: 0; }
  .card-front .brand {
    position: absolute; left: 36px; top: 58px;
    display: flex; align-items: center; gap: 14px;
  }
  .card-front .brand-dot {
    width: 52px; height: 52px; border-radius: 50%; background: var(--teal);
  }
  .card-front .brand-name {
    color: var(--teal); font-weight: 900; font-size: 24px; letter-spacing: 0.3px;
  }
  .address {
    position: absolute; right: 26px; top: 176px;
    text-align: right; color: var(--ink-grey); font-size: 12.5px; line-height: 1.45;
  }
  .contact { position: absolute; left: 30px; top: 194px; }
  .contact .person {
    color: var(--teal); font-weight: 700; font-size: 17px; letter-spacing: 0.5px; line-height: 1.2;
  }
  .contact .credentials, .contact .role {
    color: var(--light-ink); font-size: 11.5px; line-height: 1.3;
  }
  .contact .lines { margin-top: 8px; }
  .contact .line {
    display: flex; align-items: center; gap: 9px;
    color: var(--light-ink); font-size: 12px; margin-top: 5px;
  }
  .contact .line svg { width: 13px; height: 13px; flex: none; }
  .website {
    position: absolute; right: 26px; bottom: 8px;
    color: var(--white); font-weight: 700; font-size: 12.5px; letter-spacing: 0.6px;
  }
</style>
</head>
<body>
<main class="canvas">

  <section class="card card-back" aria-label="Business card back">
    <div class="brand">
      <span class="brand-dot"></span>
      <span class="brand-name">Silverbrook Pet Vision Care</span>
    </div>
  </section>

  <section class="card card-front" aria-label="Business card front">
    <svg class="shapes" viewBox="0 0 560 320" width="560" height="320" aria-hidden="true">
      <!-- charcoal lower field -->
      <path d="M0 170 C 200 150, 400 215, 560 275 L560 320 L0 320 Z" fill="var(--charcoal)"/>
      <!-- teal rim along the charcoal field -->
      <path d="M0 162 C 200 142, 400 207, 560 266 L560 275 C 400 215, 200 150, 0 170 Z" fill="var(--teal)"/>
      <!-- upper swoosh -->
      <path d="M230 160 C 370 168, 480 140, 560 92 L560 102 C 480 152, 370 174, 230 160 Z" fill="var(--teal)"/>
      <!-- bottom band -->
      <path d="M160 320 C 300 294, 440 284, 560 280 L560 320 Z" fill="var(--teal)"/>
    </svg>

    <div class="brand">
      <span class="brand-dot"></span>
      <span class="brand-name">Silverbrook Pet Vision Care</span>
    </div>

    <div class="address">1875 Tessock Rd,<br>Kelowna, BC, V4T 8M3</div>

    <div class="contact">
      <div class="person">MARISOL QUENT</div>
      <div class="credentials">BSc, DVM, MSc, DipACVO</div>
      <div class="role">Veterinary Ophthalmologist</div>
      <div class="lines">
        <div class="line">
          <svg viewBox="0 0 16 16" aria-hidden="true"><path fill="var(--teal)" d="M3 2h3l1.5 3.5-2 1.2a8 8 0 0 0 3.8 3.8l1.2-2L14 10v3a1 1 0 0 1-1 1A11 11 0 0 1 2 3a1 1 0 0 1 1-1z"/></svg>
          <span>250.419.3067</span>
        </div>
        <div class="line">
          <svg viewBox="0 0 16 16" aria-hidden="true"><rect x="1" y="3" width="14" height="10" rx="1" fill="var(--teal)"/><path d="M1.5 3.8 8 9l6.5-5.2" fill="none" stroke="var(--charcoal)" stroke-width="1.3"/></svg>
          <span>silverbrookpetvisioncare@mailvero.com</span>
        </div>
      </div>
    </div>

    <div class="website">www.silverbrookpetvisioncare.com</div>
  </section>

</main>
</body>
</html>
```